BRIM Outreach Partners Business Card Rebrand

Hello Designers! We are looking for help designing our new business card to go in conjunction with our company rebrand. Unfortunately, we have an event mid June that requires we get these printed ASAP (before our new website is launched.) We have a mostly complete Brand Book which I have uploaded to this request for your reference to company information, style, fonts. I've also enclosed our logo file in .eps & .jpg. Attached is a sample business card my boss liked but said was "too simple." I made it in Canva and do not profess to be a designer. NOT FOR DESIGN REFERENCE, ONLY FOR CONTEXT Here is what our old website looks like: https://brimoutreachpartners.com/.

```html
<!DOCTYPE html>
<html lang="en">
<head>
<meta charset="utf-8">
<title>BRIM Outreach Partners – Business Card</title>
<link rel="stylesheet" href="https://fonts.googleapis.com/css2?family=Jost:wght@400;500;600;700&display=swap">
<style>
  :root {
    --page-bg: #e9e7e4;
    --dark-top: #22313a;
    --dark-bottom: #0a1012;
    --card-white: #ffffff;
    --card-fade: #f1f2f3;
    --brand-blue: #3e9fd1;
    --faint-blue: #e3eef6;
    --ink: #111416;
    --text-grey: #3c4146;
    --rule: #8a8f94;
    --on-dark: #f2f4f5;
  }
  * { box-sizing: border-box; margin: 0; padding: 0; }
  html, body { width: 1200px; height: 900px; overflow: hidden; }
  body {
    background: var(--page-bg);
    font-family: "Jost", "Futura", sans-serif;
    display: flex;
    flex-direction: column;
    align-items: center;
    justify-content: center;
    gap: 50px;
  }
  .card {
    position: relative;
    width: 640px;
    height: 366px;
    border-radius: 34px;
    overflow: hidden;
    box-shadow: 0 14px 30px rgba(0,0,0,.22);
  }

  /* Back side */
  .card--back {
    background: radial-gradient(ellipse at 40% 55%, var(--dark-top) 0%, var(--dark-bottom) 75%);
    display: flex;
    align-items: center;
    justify-content: center;
  }
  .brand-lockup {
    display: flex;
    align-items: center;
    gap: 18px;
  }
  .brand-lockup__dot {
    flex: none;
    border-radius: 50%;
  }
  .brand-lockup__name {
    font-weight: 600;
    line-height: 1.02;
    letter-spacing: .01em;
  }
  .card--back .brand-lockup__dot { width: 92px; height: 92px; background: var(--on-dark); }
  .card--back .brand-lockup__name { color: var(--on-dark); font-size: 40px; }

  /* Front side */
  .card--front {
    background: linear-gradient(115deg, var(--card-white) 0%, var(--card-fade) 55%, var(--card-white) 100%);
  }
  .front__backdrop-circle {
    position: absolute;
    width: 270px;
    height: 270px;
    border-radius: 50%;
    background: var(--faint-blue);
    right: 70px;
    top: -40px;
  }
  .contact-block {
    position: absolute;
    left: 44px;
    top: 40px;
  }
  .contact-block__name {
    color: var(--brand-blue);
    font-weight: 600;
    font-size: 24px;
    letter-spacing: .03em;
    text-transform: uppercase;
  }
  .contact-block__title {
    color: var(--text-grey);
    font-size: 17px;
    margin-top: 2px;
  }
  .contact-list {
    list-style: none;
    margin-top: 18px;
  }
  .contact-list li {
    display: flex;
    align-items: center;
    gap: 12px;
    color: var(--text-grey);
    font-size: 17px;
    line-height: 1.65;
  }
  .contact-list svg { width: 18px; height: 18px; flex: none; }
  .divider {
    position: absolute;
    left: 44px;
    width: 360px;
    height: 1px;
    background: var(--rule);
  }
  .divider--top { top: 30px; left: 310px; width: 0; }
  .divider--mid { top: 218px; }
  .card--front .brand-lockup {
    position: absolute;
    left: 56px;
    bottom: 30px;
  }
  .card--front .brand-lockup__dot { width: 96px; height: 96px; background: var(--brand-blue); }
  .card--front .brand-lockup__name { color: var(--ink); font-size: 38px; }
  .location {
    position: absolute;
    right: 44px;
    top: 190px;
    text-align: right;
    color: var(--text-grey);
    font-size: 17px;
    line-height: 1.35;
  }
</style>
</head>
<body>

  <section class="card card--back" aria-label="Business card, back">
    <div class="brand-lockup">
      <span class="brand-lockup__dot"></span>
      <span class="brand-lockup__name">BRIM Outreach<br>Partners</span>
    </div>
  </section>

  <section class="card card--front" aria-label="Business card, front">
    <div class="front__backdrop-circle"></div>

    <div class="contact-block">
      <h1 class="contact-block__name">Jordan Wells-Hart</h1>
      <p class="contact-block__title">Managing Partner</p>
      <ul class="contact-list">
        <li>
          <svg viewBox="0 0 24 24" aria-hidden="true"><path fill="#3e9fd1" d="M6.6 10.8a15.1 15.1 0 0 0 6.6 6.6l2.2-2.2c.3-.3.7-.4 1-.2 1.1.4 2.3.6 3.6.6.6 0 1 .4 1 1V20c0 .6-.4 1-1 1A17 17 0 0 1 3 4c0-.6.4-1 1-1h3.5c.6 0 1 .4 1 1 0 1.3.2 2.5.6 3.6.1.3 0 .7-.2 1z"/></svg>
          +555-014-2290
        </li>
        <li>
          <svg viewBox="0 0 24 24" aria-hidden="true"><rect x="2" y="5" width="20" height="14" rx="1.5" fill="#3e9fd1"/><path d="M3 6l9 7 9-7" fill="none" stroke="#fff" stroke-width="1.6"/></svg>
          jordan@brimoutreachpartners.com
        </li>
        <li>
          <svg viewBox="0 0 24 24" aria-hidden="true" fill="none" stroke="#3e9fd1" stroke-width="1.6"><circle cx="12" cy="12" r="9"/><ellipse cx="12" cy="12" rx="4" ry="9"/><path d="M3 12h18M5 7h14M5 17h14"/></svg>
          www.brimoutreachpartners.com
        </li>
      </ul>
    </div>

    <div class="divider divider--mid"></div>

    <p class="location">Denver, CO based<br>( Mountain Time )</p>

    <div class="brand-lockup">
      <span class="brand-lockup__dot"></span>
      <span class="brand-lockup__name">BRIM Outreach<br>Partners</span>
    </div>
  </section>

</body>
</html>
```